Perfume label

For a new perfume label I need a label design and box design for a square bottle

What to include on the label
Name: Bel-Qamir, House of Mists
Fragrance description : Oudh, Roses
Fragrance number: 1
50ml
Perfume ingredient list on the box

Square bottle and Box

Label design preferences: Modern minimalistic with a little luxury touch.
Label to cover two sides of the box (wrap around) refer to drawing in attachment. Both on the box as the bottle.

```html
<!DOCTYPE html>
<html lang="en">
<head>
<meta charset="utf-8">
<title>Bel-Qamir — Rose Label</title>
<link href="https://fonts.googleapis.com/css2?family=Cinzel:wght@400;600&family=Marcellus&family=Montserrat:wght@300&display=swap" rel="stylesheet">
<style>
  :root {
    --backdrop: #808184;
    --label: #ffffff;
    --gold: #c9973a;
    --gold-light: #f2d67e;
    --gold-deep: #a06a18;
    --ink: #3a3a3c;
    --ink-soft: #5a5a5c;
    --blush: #f8d3cf;
    --blush-deep: #f2a9a3;
    --blush-pale: #fcefee;
  }
  * { margin: 0; padding: 0; box-sizing: border-box; }
  html, body {
    width: 1053px;
    height: 1200px;
    overflow: hidden;
    background: var(--backdrop);
  }
  .label {
    position: absolute;
    left: 172px;
    top: 129px;
    width: 709px;
    height: 942px;
    background: var(--label);
    border-radius: 32px;
    overflow: hidden;
  }
  .rose-haze {
    position: absolute;
    left: 70px;
    top: 200px;
    width: 560px;
    height: 560px;
    border-radius: 50%;
    background: radial-gradient(circle at 50% 50%, rgba(252,239,238,0.9) 0%, rgba(255,255,255,0) 70%);
  }
  .rose-art {
    position: absolute;
    left: 106px;
    top: 313px;
    width: 490px;
    height: 490px;
    border-radius: 50%;
    background: radial-gradient(circle at 50% 50%, var(--blush-deep) 0%, var(--blush) 20%, var(--blush-pale) 52%, rgba(255,255,255,0) 70%);
  }
  .leaves-top {
    position: absolute;
    right: -50px;
    top: 40px;
    width: 200px;
    height: 360px;
    border-radius: 50%;
    background: radial-gradient(ellipse at 55% 50%, rgba(246,201,198,0.4) 0%, rgba(255,255,255,0) 70%);
  }
  .leaves-bottom {
    position: absolute;
    left: -50px;
    bottom: -30px;
    width: 190px;
    height: 230px;
    border-radius: 50%;
    background: radial-gradient(ellipse at 45% 55%, rgba(246,201,198,0.4) 0%, rgba(255,255,255,0) 70%);
  }
  .brand-name {
    position: absolute;
    left: 0; right: 0;
    top: 76px;
    text-align: center;
    font-family: "Cinzel", serif;
    font-weight: 400;
    font-size: 80px;
    line-height: 1;
    letter-spacing: 7px;
    padding-left: 7px;
    color: var(--gold);
  }
  .brand-tagline {
    position: absolute;
    left: 0; right: 0;
    top: 168px;
    text-align: center;
    font-family: "Montserrat", sans-serif;
    font-weight: 300;
    font-size: 28px;
    line-height: 1;
    letter-spacing: 15px;
    padding-left: 15px;
    color: var(--ink);
  }
  .scent-name {
    position: absolute;
    left: 0; right: 0;
    top: 292px;
    text-align: center;
    font-family: "Cinzel", serif;
    font-weight: 600;
    font-size: 138px;
    line-height: 1;
    background: linear-gradient(180deg, var(--gold-light) 0%, var(--gold) 40%, var(--gold-deep) 68%, var(--gold-light) 100%);
    -webkit-background-clip: text;
    background-clip: text;
    color: transparent;
  }
  .gold-rule {
    position: absolute;
    left: 311px;
    top: 434px;
    width: 88px;
    height: 2px;
    background: var(--gold);
  }
  .volume {
    position: absolute;
    left: 0; right: 0;
    top: 856px;
    text-align: center;
    font-family: "Marcellus", serif;
    font-size: 40px;
    line-height: 1;
    color: var(--ink-soft);
  }
</style>
</head>
<body>
  <main class="label">
    <div class="rose-haze" role="img" aria-label="Soft watercolour wash of pale pink petals"></div>
    <div class="leaves-top" role="img" aria-label="Faint watercolour leaves and splashes in blush pink"></div>
    <div class="leaves-bottom" role="img" aria-label="Faint watercolour leaves in blush pink"></div>
    <div class="rose-art" role="img" aria-label="Watercolour illustration of a pink rose in full bloom"></div>

    <h1 class="brand-name">BEL-QAMIR</h1>
    <p class="brand-tagline">HOUSE OF MISTS</p>
    <h2 class="scent-name">ROSE</h2>
    <div class="gold-rule"></div>
    <p class="volume">50ML(1.7FLOZ)</p>
  </main>
</body>
</html>
```